WHAT LIES BEYOND? Discovering the shape of days with the Silent Lamp

Creating a book that is about living a spiritual life. The book is about letting go of the materialistic world and finding happiness through self realisation and enlightenment. The contents page is below that gives an idea of what is contained in the book.

The book is based on the writings of the Sikhs - from India. But it is written in a universal way that is understandable to all.

CONTENTS
Living for a purpose
- Born to be original! Dying as a copy!
- My relationship with everything but me!
- What is my purpose?

Life as a human being!
- Stages of Life
- Five Weaknesses

What is driving our lives?
- Information overload?
- What are your drivers?
- Giving life meaning

You reap what you sow
- Is my destiny written?
- Good and bad actions
- Maya – the illusion and it’s three modes

Slow down and let go
- The mind in overdrive
- Being aware of our mental health
- Why Slow Down?

The Guidance of the Guru
- Why do I need a Guru?
- What the Guru gives you
- Gurbani – the Guru’s Words

Staying connected
- Repeating the Mantra
- Doing two things at once
- Remembering in times of difficulty

Cultivating virtues
- Theory vs Practice
- Virtues and true religion
- Some key virtues

The Mystical Creation
- Experiencing ecstasy
- Enlightenment and intuition
- Spiritual Transformation

Good Company
- How do my companions affect me?
- The company of Saintly people
- Obtaining the fruits that the Guru describes

Serving selflessly
- Serving is our purpose
- Being grateful
- Being generous

Ten things to change your life today

Target Market(s)

All those who want to learn about spirituality. We are targeting young and middle aged but not necessarily ruling out older demographic.

Requirements
Must have
• The book cover:

- exciting and intriguing
- theme is "what lies beyond" in this world
- some kind of lean towards enlightenment
Nice to have
• It is not essential but the cover could subtly show something about the Sikh faith. Can discuss this further if necessary.
Should not have
• Should not:

- look dull and boring
- don't want it to look like a Buddhism book

```html
<!DOCTYPE html>
<html lang="en">
<head>
<meta charset="utf-8">
<title>What Lies Beyond? — Book Cover</title>
<link rel="stylesheet" href="https://fonts.googleapis.com/css2?family=Cinzel:wght@400;500&display=swap">
<style>
  :root {
    --page-bg: #eeeeee;
    --cover-deep: #06142a;
    --cover-mid: #0d2a52;
    --cover-blue: #1a4f86;
    --glow: #9fd4ff;
    --glow-soft: rgba(120, 190, 255, 0.55);
    --text-light: #f4f6fa;
    --text-sub: #e4ecf6;
  }
  * { margin: 0; padding: 0; box-sizing: border-box; }
  html, body {
    width: 1200px;
    height: 1200px;
    overflow: hidden;
    background: var(--page-bg);
  }
  .canvas {
    position: relative;
    width: 1200px;
    height: 1200px;
    display: flex;
    align-items: center;
    justify-content: center;
  }
  .cover {
    position: relative;
    width: 700px;
    height: 1110px;
    overflow: hidden;
    background:
      radial-gradient(ellipse 18% 30% at 55% 0%, rgba(200, 235, 255, 0.85), rgba(120, 190, 255, 0.25) 55%, transparent 100%),
      radial-gradient(ellipse 45% 60% at 55% 20%, rgba(60, 130, 200, 0.45), transparent 75%),
      radial-gradient(ellipse 60% 40% at 50% 78%, rgba(40, 110, 190, 0.45), transparent 80%),
      linear-gradient(180deg, var(--cover-mid) 0%, var(--cover-deep) 55%, #040d1c 100%);
    font-family: "Cinzel", "Trajan Pro", serif;
    color: var(--text-light);
    text-align: center;
  }
  .light-beam {
    position: absolute;
    left: 0; top: 0;
    width: 100%; height: 100%;
  }
  .title {
    position: absolute;
    top: 95px;
    left: 0; right: 0;
    font-weight: 400;
    font-size: 84px;
    line-height: 112px;
    letter-spacing: 3px;
    text-shadow: 0 3px 8px rgba(0, 0, 0, 0.55);
  }
  .subtitle {
    position: absolute;
    top: 362px;
    left: 0; right: 0;
    font-weight: 400;
    font-size: 28px;
    line-height: 46px;
    letter-spacing: 1.5px;
    color: var(--text-sub);
    text-shadow: 0 2px 6px rgba(0, 0, 0, 0.5);
  }
  .meditation-art {
    position: absolute;
    left: 210px;
    top: 760px;
    width: 300px;
    height: 300px;
    border-radius: 50%;
    background:
      radial-gradient(circle at 50% 35%, var(--glow) 0%, var(--glow-soft) 22%, rgba(30, 90, 160, 0.45) 50%, transparent 72%);
  }
  .author {
    position: absolute;
    bottom: 62px;
    left: 0; right: 0;
    font-weight: 400;
    font-size: 40px;
    letter-spacing: 4px;
    color: var(--text-light);
  }
</style>
</head>
<body>
  <main class="canvas">
    <section class="cover">
      <svg class="light-beam" viewBox="0 0 700 1110" aria-hidden="true">
        <defs>
          <linearGradient id="beamFade" x1="0" y1="0" x2="0" y2="1">
            <stop offset="0" stop-color="#d8f0ff" stop-opacity="0.55"/>
            <stop offset="0.5" stop-color="#6fb4ef" stop-opacity="0.12"/>
            <stop offset="1" stop-color="#6fb4ef" stop-opacity="0"/>
          </linearGradient>
        </defs>
        <polygon points="365,0 405,0 470,760 300,760" fill="url(#beamFade)"/>
        <polygon points="375,0 395,0 420,520 350,520" fill="url(#beamFade)"/>
      </svg>

      <h1 class="title">WHAT LIES<br>BEYOND?</h1>
      <p class="subtitle">DISCOVERING THE SHAPE OF DAYS<br>WITH THE SILENT LAMP</p>

      <div class="meditation-art" role="img" aria-label="Silhouette of a person seated in meditation, lit from behind by a soft blue glow"></div>

      <p class="author">AUTHOR NAME</p>
    </section>
  </main>
</body>
</html>
```